Derek Holloway Resume

Need to update resume with latest position and ensure it stays to 2 pages, may need advice on what to get rid of and simply clean it up, already have a format that i like but am open to change but don't want to spend a fortune

```html
<!DOCTYPE html>
<html lang="en">
<head>
<meta charset="utf-8">
<title>Derek W. Holloway – Resume</title>
<link rel="stylesheet" href="https://fonts.googleapis.com/css2?family=Noto+Sans:wght@400;700&display=swap">
<style>
  :root {
    --ink: #111111;
    --navy: #1d2d6b;
    --rule: #9a9a9a;
    --rule-dark: #4a4a4a;
    --band: #e4e4e4;
    --band-light: #ececec;
    --page: #ffffff;
  }
  * { margin: 0; padding: 0; box-sizing: border-box; }
  html, body { width: 946px; height: 1200px; overflow: hidden; background: var(--page); }
  body { font-family: "Noto Sans", Tahoma, sans-serif; color: var(--ink); position: relative; }
  .block { position: absolute; left: 42px; width: 862px; }

  .name { top: 30px; font-size: 31px; font-variant: small-caps; letter-spacing: 2.5px; color: var(--navy); text-align: center; line-height: 1; font-weight: 400; }
  .contact { top: 72px; font-size: 13.5px; font-weight: 700; text-align: center; }
  .contact .sep { display: inline-block; width: 5px; height: 5px; background: var(--ink); margin: 0 8px; vertical-align: 3px; }
  .rule { height: 2px; background: var(--rule); }
  .headline { top: 111px; font-size: 18px; font-weight: 700; font-variant: small-caps; letter-spacing: 1.5px; color: var(--navy); text-align: center; }
  .tagline { top: 141px; height: 50px; background: var(--band); border-top: 3px solid var(--rule-dark); border-bottom: 3px solid var(--rule-dark); font-size: 13.5px; font-weight: 700; display: flex; align-items: center; justify-content: center; }
  .summary { top: 199px; left: 42px; width: 862px; font-size: 13.3px; font-weight: 700; line-height: 17px; text-align: center; white-space: nowrap; }
  .highlights { top: 262px; left: 72px; width: 820px; list-style: none; font-size: 15.3px; line-height: 22.5px; }
  .highlights li { position: relative; padding-left: 29px; }
  .highlights li::before { content: ""; position: absolute; left: 4px; top: 8px; width: 8px; height: 8px; border: 1.2px solid var(--ink); box-shadow: 1px 1px 0 var(--ink); }
  .competency-label { top: 334px; font-size: 13px; text-align: center; }
  .competencies { top: 360px; height: 97px; background: var(--band); font-size: 14.2px; font-weight: 700; line-height: 20.6px; text-align: center; padding-top: 8px; text-shadow: 0 0 1px #fff; }

  .section-title { top: 484px; font-size: 22px; font-weight: 700; font-variant: small-caps; letter-spacing: 3px; color: var(--navy); text-align: center; }

  .employer { font-size: 17px; font-weight: 700; text-align: center; }
  .employer .sep { display: inline-block; width: 8px; height: 8px; background: var(--ink); margin: 0 6px; vertical-align: 2px; }
  .role { height: 28px; background: var(--band-light); font-size: 15.5px; font-weight: 700; display: flex; align-items: center; justify-content: center; }
  .scope { font-size: 13.4px; line-height: 17.5px; text-align: justify; }
  .result { font-size: 13.4px; font-weight: 700; color: var(--navy); text-align: center; }
  .duties { list-style: none; font-size: 13.4px; line-height: 17.5px; }
  .duties li { position: relative; padding-left: 42px; margin-bottom: 6px; text-align: justify; }
  .duties li::before { content: ""; position: absolute; left: 23px; top: 6px; width: 5px; height: 5px; background: var(--ink); }
  .continued { top: 1148px; font-size: 13.4px; text-align: right; }
</style>
</head>
<body>
  <h1 class="block name">Derek W. Holloway</h1>
  <p class="block contact">1417 Larkspur Lane<span class="sep"></span>Ashbury, VA 24410<span class="sep"></span>757.555.0142<span class="sep"></span>derekholloway@mailbox.com</p>
  <div class="block rule" style="top:100px"></div>
  <h2 class="block headline">Award-Winning Sales Manager</h2>
  <div class="block tagline">Driving exceptional levels of sales results in competitive industries and changing environments.</div>
  <p class="block summary">Aggressive, loyal, energetic sales leader with a history of turning around underperforming teams,<br>departments, and territories. Proven consultative sales approach with a focus on product knowledge, trust,<br>and superior service. Strong interpersonal, communication, presentation, and analytical skills.</p>
  <ul class="block highlights">
    <li>Developed effective sales incentives and initiatives that became company-wide best practices.</li>
    <li>Drove revenue growth at direct, indirect, and retail sales levels; won multiple prestigious awards.</li>
    <li>Recruited, developed, trained, and motivated high-energy sales/customer support teams.</li>
  </ul>
  <p class="block competency-label">CORE COMPETENCIES INCLUDE:</p>
  <div class="block competencies">
    New Business Development | C-Level Relationship Building | Complex Solution Selling<br>
    High-Impact Sales Presentations | B2C &amp; B2B Channels | Machine to Machine Technology<br>
    Channel Manager | Performance Management | Competitive Analysis | CRM Platforms<br>
    Territory Sales Management | SaaS | Budgeting &amp; Forecasting | Vendor Management
  </div>

  <div class="block rule" style="top:475px"></div>
  <h2 class="block section-title">Career History</h2>
  <div class="block rule" style="top:514px;height:1.5px"></div>

  <section class="block" style="top:524px">
    <h3 class="employer">Veridian Telecom<span class="sep"></span>April 2016- Present</h3>
    <div class="role" style="margin-top:6px">Regional Sales and Marketing Manager: Mid Atlantic</div>
    <p class="scope" style="margin-top:9px">Lead a team of sales managers and vendor partners responsible for driving Veridian FiberLine sales and revenue growth in over 200 Big Box locations throughout Virginia, Maryland, DC, New Jersey, Delaware, and Pennsylvania.</p>
    <ul class="duties" style="margin-top:6px">
      <li><b>Top Performer:</b> #1 RSM in the country in 4Q 2016 and Q1 2017 based on quota performance and revenue growth.</li>
      <li><b>Retailer Partnerships:</b> Negotiated a 1st time no cost self-service Veridian kiosk inside the #1 retailer in the world resulting in a 200% increase in FiberLine sales.</li>
      <li>Set strategy and determine implementation plan to penetrate Veridian opportunity in the National Big Box retailer channel. Lead and support the business partner relationship to ignite growth and optimize our customer experience.</li>
      <li><b>Business Development -</b> Q2 Successfully negotiated and launched FiberLine in Tarvell as a new partner.</li>
    </ul>
  </section>

  <section class="block" style="top:765px">
    <h3 class="employer">Tessaro<span class="sep"></span>2014</h3>
    <div class="role" style="margin-top:6px">Developmental Executive</div>
    <p class="scope" style="margin-top:7px">Sell wireless portfolio to the Northgate Defense Agency, Office of Coastal Readiness, Bureau of Civic Affairs, Brook Ashford Group, and Bellmont Aerospace.</p>
    <p class="result" style="margin-top:6px">Increased overall revenue in assigned agencies 101.8% YOY.</p>
    <ul class="duties" style="margin-top:5px">
      <li><b>Wireless Solutions:</b> Facilitate critical communications for public-sector agencies through wireless solutions for networks, infrastructures, and security and surveillance.</li>
      <li><b>Government Contracts:</b> Navigate complex matrix of budgeting, bidding, and procurement for government contracts.</li>
      <li><b>Collaboration:</b> Work closely with solution engineers, project managers, and C-level executives on identifying the best solutions for their organizations.</li>
    </ul>
  </section>

  <section class="block" style="top:1009px">
    <h3 class="employer">Allton Networks<span class="sep"></span>2014</h3>
    <div class="role" style="margin-top:6px">Client Business Manager</div>
    <p class="scope" style="margin-top:7px">Held national responsibility for sales of the entire Allton Networks solutions portfolio to Meridian Reserve Trust. Solutions included mobility, professional services, IP, Cloud, SaaS, Network Infrastructure, and Managed Solutions.</p>
    <p class="result" style="margin-top:6px">Sold nationwide managed Wi-Fi solution for all 12 Meridian Reserve Trust locations.</p>
  </section>

  <p class="block continued">Continued…</p>
</body>
</html>
```